Education Certificate

We need a modern yet professional Certificate for those who successfully pass / complete our online Training course.

There are various courses but ONE certificate design required.

the certificate needs to look extremely professional and of value.

```html
<!DOCTYPE html>
<html lang="en">
<head>
<meta charset="utf-8">
<title>Certificate of Completion</title>
<link href="https://fonts.googleapis.com/css2?family=Arimo:ital,wght@0,400;0,700;1,700&family=Open+Sans:wght@700&family=Playfair+Display:wght@900&family=Great+Vibes&display=swap" rel="stylesheet">
<style>
  :root {
    --royal: #0a3596;
    --ribbon: #00349a;
    --gold: #ffd200;
    --paper: #ffffff;
    --backdrop: #f1f1f1;
    --brand-fill: #234fa8;
  }
  html, body {
    margin: 0;
    padding: 0;
    width: 1200px;
    height: 848px;
    overflow: hidden;
    background: var(--paper);
  }
  .certificate {
    position: relative;
    width: 1200px;
    height: 848px;
    background: var(--paper);
    font-family: "Arimo", Arial, sans-serif;
    color: var(--royal);
  }
  .brand-box {
    position: absolute;
    left: 85px;
    top: 88px;
    width: 175px;
    height: 120px;
    background: var(--brand-fill);
    display: flex;
    align-items: center;
    padding-left: 18px;
    box-sizing: border-box;
    gap: 10px;
  }
  .brand-mark {
    width: 14px;
    height: 14px;
    background: var(--gold);
    flex: none;
  }
  .brand-name {
    font-weight: 700;
    font-size: 13px;
    line-height: 1.15;
    color: #ffffff;
  }
  .heading-divider {
    position: absolute;
    left: 281px;
    top: 108px;
    width: 2px;
    height: 77px;
    background: var(--royal);
  }
  .heading {
    position: absolute;
    left: 305px;
    top: 92px;
    margin: 0;
    font-family: "Playfair Display", Georgia, serif;
    font-weight: 900;
    color: #00339c;
    line-height: 1;
  }
  .heading-main {
    display: block;
    font-size: 70px;
  }
  .heading-sub {
    display: block;
    font-size: 27px;
    margin-top: -2px;
    padding-left: 2px;
  }
  .recipient {
    position: absolute;
    left: 82px;
    top: 279px;
    margin: 0;
    font-family: "Open Sans", Arial, sans-serif;
    font-weight: 700;
    font-size: 74px;
    line-height: 1;
    color: var(--gold);
  }
  .lead {
    position: absolute;
    left: 87px;
    top: 356px;
    margin: 0;
    font-size: 19px;
  }
  .course-title {
    position: absolute;
    left: 86px;
    top: 405px;
    margin: 0;
    font-size: 19.5px;
    font-weight: 700;
    letter-spacing: 0.2px;
  }
  .course-text {
    position: absolute;
    left: 86px;
    width: 632px;
    margin: 0;
    font-size: 17px;
    line-height: 19px;
  }
  .course-text.first { top: 439px; }
  .course-text.second { top: 496px; }
  .completion-date {
    position: absolute;
    left: 86px;
    top: 580px;
    margin: 0;
    font-size: 22px;
  }
  .signature {
    position: absolute;
    left: 92px;
    top: 672px;
    font-family: "Great Vibes", cursive;
    font-size: 32px;
    color: #152a6e;
    line-height: 1;
  }
  .signature-line {
    position: absolute;
    left: 86px;
    top: 719px;
    width: 194px;
    height: 1px;
    background: var(--royal);
  }
  .signatory-role {
    position: absolute;
    left: 131px;
    top: 725px;
    margin: 0;
    font-weight: 700;
    font-style: italic;
    font-size: 16px;
  }
  .award-art {
    position: absolute;
    left: 0;
    top: 0;
  }
</style>
</head>
<body>
  <main class="certificate">
    <svg class="award-art" width="1200" height="848" viewBox="0 0 1200 848">
      <defs>
        <filter id="seal-shadow" x="-30%" y="-30%" width="160%" height="160%">
          <feDropShadow dx="0" dy="4" stdDeviation="8" flood-color="#000" flood-opacity="0.25"/>
        </filter>
      </defs>
      <rect x="792" y="149" width="408" height="609" rx="40" fill="var(--backdrop)" role="img" aria-label="Faint academy emblem backdrop"/>
      <polygon points="943,0 1113,0 1113,651 1028,585 943,651" fill="var(--ribbon)"/>
      <circle cx="1030" cy="332" r="122" fill="var(--ribbon)" filter="url(#seal-shadow)" role="img" aria-label="Completion seal"/>
    </svg>

    <div class="brand-box">
      <span class="brand-mark"></span>
      <span class="brand-name">Global Service<br>Excellence<br>Academy</span>
    </div>
    <div class="heading-divider"></div>
    <h1 class="heading">
      <span class="heading-main">Certificate</span>
      <span class="heading-sub">of Completion</span>
    </h1>

    <h2 class="recipient">Amelia Carter</h2>
    <p class="lead">has completed the following course:</p>

    <h3 class="course-title">DIGITAL SERVICE EXPERIENCE FRAMEWORK DSEF2024</h3>
    <p class="course-text first">DSEF2024 reflects the increased international growth in scale, reach and scope of digital transformation and services delivered through Digital Channels.</p>
    <p class="course-text second">The primary aim of the DSEF2024 Framework is to motivate organisations to focus their attention on the Digital Customer Experience through the delivery of service excellence techniques</p>

    <p class="completion-date">on March 20, 2024</p>

    <div class="signature">Marcus Ellery</div>
    <div class="signature-line"></div>
    <p class="signatory-role">CEO, gsxa</p>
  </main>
</body>
</html>
```